Home page web design for "Tales from Thee"

We need a home page web design for a start up company that will write memoirs for seniors.
The completed project will need to include PSD files...NO HTML or CSS necessary.
Attached is a brief outline concept that may give you some ideas...but you are the creative professionals, so please feel free to add your ideas. We will also attach some files that show you our logo, brochures, and photos that could be used to give you ideas of our focus.
There will need to be access to the other pages on the home page to include: 'About Us'; 'How We Can Help'; 'Community Sessions'; 'Senior Consulting ' and 'Contact Us'.
Updates

Target Market(s)

Seniors and Baby Boomers

Industry/Entity Type

It Company

Number of Pages Required

1 page

Colors
f9ba93
fbca95
faa54b
faf289
f37123

Requirements
Must have
• Script easy on senior eyes.
• Initial contact number would be 844-4LANTERN
Nice to have
• While the color pallet is non-specific we prefer the warm colors.
• salmon, peach.......
• NOT so much the orange of Halloween:)
• However, please utilize your creativity and put in colors you feel will draw best with your design.

```html
<!DOCTYPE html>
<html lang="en">
<head>
<meta charset="utf-8">
<title>Tales from Thee — Home</title>
<link rel="stylesheet" href="https://fonts.googleapis.com/css2?family=Cormorant+Garamond:ital,wght@1,500;1,600&family=Open+Sans:wght@400;600&display=swap">
<style>
:root{
  --gold:#7a5c24;
  --gold-light:#c9b27a;
  --text:#4a4a4a;
  --band:#785b2a;
  --field:#56401d;
  --field-text:#b9a37a;
  --hero-bg:#ecebe8;
  --section-bg:#ececec;
  --submit-a:#ffb300;
  --submit-b:#f58a00;
  --white:#ffffff;
}
*{box-sizing:border-box;margin:0;padding:0}
html,body{width:1175px;height:1200px;overflow:hidden;background:var(--white);font-family:"Open Sans",sans-serif;color:var(--text)}
.page{position:relative;width:1175px;height:1200px}

.site-header{position:absolute;top:0;left:0;width:1175px;height:86px;background:var(--white);box-shadow:0 2px 4px rgba(0,0,0,.12);z-index:2}
.header-phone{position:absolute;left:139px;top:16px;display:flex;align-items:center;gap:10px;font-size:17px;font-weight:600;color:var(--gold)}
.header-phone .dot{width:24px;height:24px;border-radius:50%;background:var(--gold-light);display:flex;align-items:center;justify-content:center}
.nav{position:absolute;top:61px;display:flex;gap:24px;font-size:12px;color:#333;letter-spacing:.2px}
.nav-left{left:137px}
.nav-right{right:137px}
.social{position:absolute;right:139px;top:16px;display:flex;gap:9px}
.social span{width:24px;height:24px;border-radius:50%;background:var(--gold-light)}
.social span:first-child{background:var(--gold)}
.brand-tab{position:absolute;left:448px;top:0;width:226px;height:132px;border-radius:0 0 113px 113px / 0 0 60px 60px;background:var(--white);box-shadow:0 3px 5px rgba(0,0,0,.14);z-index:3;display:flex;align-items:center;justify-content:center}
.brand-name{font-family:"Open Sans",sans-serif;font-weight:600;font-size:19px;color:var(--gold)}

.hero{position:absolute;top:86px;left:0;width:1175px;height:395px;background:linear-gradient(90deg,#e4e2de 0%,#f1f0ee 60%,#e9e6df 100%)}
.hero-photo{position:absolute;left:0;top:0;width:560px;height:395px;background:linear-gradient(120deg,#e6e6e6 0%,#9aa8b5 30%,#6a8fa8 50%,#caa890 70%,#e8e6e2 100%)}
.hero-title{position:absolute;left:591px;top:112px;font-family:"Cormorant Garamond",serif;font-style:italic;font-weight:600;font-size:45px;line-height:50px;color:var(--gold)}
.btn-outline{position:absolute;left:591px;top:267px;width:112px;height:33px;border:1px solid var(--gold);color:var(--gold);font-size:13px;font-weight:600;display:flex;align-items:center;justify-content:center}

.about{position:absolute;top:481px;left:0;width:1175px;height:461px;background:var(--section-bg)}
.about-portrait{position:absolute;left:176px;top:27px;width:170px;height:170px;border-radius:50%;border:4px solid var(--white);box-shadow:0 0 0 1px #bbb;background:radial-gradient(circle at 45% 45%,#b08a6a 0%,#6a4a32 55%,#3a2a1c 100%)}
.about-title{position:absolute;left:360px;top:28px;font-family:"Cormorant Garamond",serif;font-style:italic;font-weight:600;font-size:31px;color:var(--gold)}
.about-rule{position:absolute;left:360px;top:72px}
.about-sub{position:absolute;left:360px;top:106px;font-size:16px;font-weight:600;color:var(--gold)}
.about-lead{position:absolute;left:360px;top:132px;width:640px;font-size:13.5px;line-height:21px}
.about-body{position:absolute;left:178px;top:216px;width:822px;font-size:13.5px;line-height:18px}
.about-body p{margin-bottom:8px}

.contact{position:absolute;top:942px;left:0;width:1175px;height:208px;background:var(--band);color:var(--white)}
.contact h2{position:absolute;top:18px;font-size:16px;font-weight:600;text-transform:uppercase}
.contact .form-title{left:178px}
.field{position:absolute;background:var(--field);border-radius:5px;color:var(--field-text);font-size:12px;padding:10px 16px}
.field-name{left:178px;top:53px;width:263px;height:37px}
.field-email{left:454px;top:53px;width:264px;height:37px}
.field-comments{left:178px;top:101px;width:438px;height:82px}
.submit{position:absolute;left:629px;top:101px;width:89px;height:82px;border-radius:5px;background:linear-gradient(135deg,var(--submit-a) 50%,var(--submit-b) 50%);color:#3a2a10;font-weight:600;font-size:14px;display:flex;align-items:center;justify-content:center}
.visit-title{left:779px}
.visit-item{position:absolute;left:779px;display:flex;gap:8px;font-size:12px;line-height:16px}

.site-footer{position:absolute;top:1150px;left:0;width:1175px;height:50px;background:var(--white);font-size:11px;color:#777}
.footer-links{position:absolute;left:185px;top:18px}
.footer-copy{position:absolute;right:177px;top:18px}
.footer-copy b{color:var(--gold);font-weight:400}
</style>
</head>
<body>
<div class="page">
  <header class="site-header">
    <div class="header-phone">
      <span class="dot"><svg width="12" height="12" viewBox="0 0 24 24"><path fill="#fff" d="M6.6 10.8a15 15 0 006.6 6.6l2.2-2.2a1 1 0 011-.25 11 11 0 003.5.6 1 1 0 011 1V20a1 1 0 01-1 1A17 17 0 013 4a1 1 0 011-1h3.5a1 1 0 011 1 11 11 0 00.6 3.5 1 1 0 01-.25 1z"/></svg></span>
      844-4LANTERN
    </div>
    <nav class="nav nav-left"><span>HOME</span><span>ABOUT US</span><span>HOW WE CAN HELP</span></nav>
    <nav class="nav nav-right"><span>COMMUNITY</span><span>SENIOR CONSULTING</span><span>CONTACT US</span></nav>
    <div class="social"><span></span><span></span><span></span><span></span><span></span></div>
  </header>
  <div class="brand-tab"><span class="brand-name">Tales from Thee</span></div>

  <section class="hero">
    <div class="hero-photo" role="img" aria-label="Photo of a grandfather reading a book with his infant grandson"></div>
    <h1 class="hero-title">Ordinary Lives.........<br>Extraordinary Legacies</h1>
    <span class="btn-outline">READ MORE</span>
  </section>

  <section class="about">
    <div class="about-portrait" role="img" aria-label="Portrait of an elderly man holding a framed keepsake"></div>
    <h2 class="about-title">Shortly about me</h2>
    <svg class="about-rule" width="265" height="12" viewBox="0 0 265 12"><circle cx="6" cy="6" r="3" fill="none" stroke="#a88c55"/><circle cx="20" cy="6" r="4" fill="none" stroke="#a88c55"/><line x1="32" y1="6" x2="265" y2="6" stroke="#c9b27a"/></svg>
    <h3 class="about-sub">When a genealogy doesn’t say enough!</h3>
    <p class="about-lead">If you were alive in 100 years, what would you share with your descendants?<br>Now you have a vehicle to help you immortalize your thoughts for the future...specifically for those who will want to know!</p>
    <div class="about-body">
      <p>We are not all presidents of countries or CEO’s of fortune 500 companies! But “every life legacy is a gift to be treasured by the next generation.”</p>
      <p>Does your family host generations of soldiers, doctors, farmers, scientists, mechanics, entrepreneurs, writers, politicians, contractors, pastors, artisans, athletes, musicians, etc..? Generational patterns can often emerge when writing your story that will interest the next generation.</p>
      <p>A genealogy, while very relevant, doesn’t offer the personal story of the names we find. A biography can place a deeper relevance on the face for future descendants. Every life is a legacy to pass forward and we at Tales from Thee believe everyone should chronicle their life journey in writing. This commitment allows you to be remembered for who you truly are as a person.</p>
      <p>Think about it....Do you know the triumphs and tribulations of your ancestors? Do you wish you did? Well, so will those falling into your personal family tree.</p>
    </div>
  </section>

  <section class="contact">
    <h2 class="form-title">Contact Us</h2>
    <div class="field field-name">Your Name:</div>
    <div class="field field-email">Email:</div>
    <div class="field field-comments">Comments:</div>
    <div class="submit">SUBMIT</div>

    <h2 class="visit-title">Visit to Tales from Thee</h2>
    <div class="visit-item" style="top:54px">
      <svg width="24" height="24" viewBox="0 0 24 24"><rect x="11" y="2" width="2.5" height="21" fill="#fff"/><path d="M3 6h17l3 2.5-3 2.5H3z" fill="#fff"/></svg>
      <span>PO Box: 4120, Amberly Lane,<br>Westhaven, Australia 654321</span>
    </div>
    <div class="visit-item" style="top:108px">
      <svg width="22" height="22" viewBox="0 0 24 24"><path fill="#fff" d="M6.6 10.8a15 15 0 006.6 6.6l2.2-2.2a1 1 0 011-.25 11 11 0 003.5.6 1 1 0 011 1V20a1 1 0 01-1 1A17 17 0 013 4a1 1 0 011-1h3.5a1 1 0 011 1 11 11 0 00.6 3.5 1 1 0 01-.25 1z"/></svg>
      <span style="padding-top:3px">555-010-2846 &nbsp;/&nbsp; 844-4LANTERN</span>
    </div>
    <div class="visit-item" style="top:160px">
      <svg width="24" height="18" viewBox="0 0 24 18"><rect x="1" y="1" width="22" height="16" fill="none" stroke="#fff" stroke-width="1.6"/><path d="M1 1l11 9 11-9" fill="none" stroke="#fff" stroke-width="1.6"/></svg>
      <span>info@talesfromthee.com</span>
    </div>
  </section>

  <footer class="site-footer">
    <div class="footer-links">Home &nbsp;/&nbsp; About Us &nbsp;/&nbsp; How We Can Help &nbsp;/&nbsp; Community &nbsp;/&nbsp; Senior Consulting &nbsp;/&nbsp; Contact Us</div>
    <div class="footer-copy">© 2014 <b>Tales from Thee.</b> &nbsp;Privacy Policy | Terms of Use</div>
  </footer>
</div>
</body>
</html>
```